Graphic Design for Free Community Event

We need a graphic created for a community event that is aimed at families with younger children called Totz Jam. This is a free event and has a fair/carnival feel to it with rides, games, and food. I need the graphic to be flexible enough to be able to be modified and used in a variety of ways on different print and digital marketing materials. I also need the centerpiece of the design to be an event logo that can be used as a standalone element.

The overall feel needs to be fun and friendly with a slightly modern edge to it. Attached are some images used in past events. These are for reference only and do not need to be simulated or used in the final product.

Target Market(s)

Families with children

Industry/Entity Type

Church

Font styles to use
Sans Serif

Requirements
Must have
• - Logo that incorporates the event name- Event Date: August 20 - Event Time: 10am - 2pm - Church name and logo incorporated: Bright Harbor Community Church (see attached logo files)
Nice to have
• - Bright colors- Flexible design elements that are interchangeable and scalable for use of the design in different layouts across different mediums and materials.
Should not have
• - Any references or images related to drugs, alcohol, tobacco, or other subjects that would be inappropriate for children.

```html
<!DOCTYPE html>
<html lang="en">
<head>
<meta charset="utf-8">
<title>Totz Jam – Bright Harbor Community Church</title>
<link rel="stylesheet" href="https://fonts.googleapis.com/css2?family=Montserrat:ital,wght@0,400;0,700;1,700;1,800;1,900&display=swap">
<style>
  :root {
    --sky: #6fd3fc;
    --rose: #ff6fa6;
    --tangerine: #f5843e;
    --butter: #f2f6c1;
    --ink: #231f20;
    --paper: #ffffff;
  }
  html, body {
    margin: 0;
    padding: 0;
    overflow: hidden;
    background: var(--paper);
  }
  .poster {
    display: block;
    width: 849px;
    height: 1200px;
    font-family: "Montserrat", Arial, sans-serif;
  }
  .church-name { font-weight: 700; fill: var(--ink); font-size: 21px; }
  .church-name--sub { font-size: 11.5px; letter-spacing: 0.3px; }
  .event-free { font-style: italic; font-weight: 800; font-size: 36px; fill: var(--butter); }
  .event-title { font-style: italic; font-weight: 900; font-size: 98px; fill: var(--butter); }
  .event-title--outline { fill: none; stroke: var(--paper); stroke-width: 1.3; }
  .event-subtitle { font-style: italic; font-weight: 900; font-size: 52px; fill: var(--paper); }
  .event-date { font-style: italic; font-weight: 800; font-size: 68px; fill: var(--paper); }
  .event-time { font-style: italic; font-weight: 800; font-size: 33px; fill: var(--paper); }
  .activity { font-style: italic; font-weight: 700; font-size: 20px; fill: var(--paper); }
</style>
</head>
<body>
<svg class="poster" viewBox="0 0 849 1200" xmlns="http://www.w3.org/2000/svg" aria-label="Totz Jam event poster">
  <defs>
    <linearGradient id="band-top" x1="0" x2="1">
      <stop offset="0" stop-color="var(--sky)"/>
      <stop offset="1" stop-color="var(--rose)"/>
    </linearGradient>
    <linearGradient id="band-bottom" x1="0" x2="1">
      <stop offset="0" stop-color="var(--rose)"/>
      <stop offset="1" stop-color="var(--sky)"/>
    </linearGradient>
    <linearGradient id="bubble" x1="0" x2="1">
      <stop offset="0" stop-color="var(--rose)"/>
      <stop offset="1" stop-color="var(--tangerine)"/>
    </linearGradient>
    <linearGradient id="badge" x1="0" x2="1">
      <stop offset="0" stop-color="var(--tangerine)"/>
      <stop offset="1" stop-color="var(--rose)"/>
    </linearGradient>
  </defs>

  <rect class="backdrop" width="849" height="1200" fill="var(--paper)"/>

  <!-- header band -->
  <circle class="band band--top" cx="424.5" cy="-229" r="449" fill="url(#band-top)"/>

  <!-- church mark -->
  <g class="church">
    <circle cx="366" cy="126" r="35" fill="var(--ink)"/>
    <text class="church-name" x="405" y="132">BRIGHT HARBOR</text>
    <text class="church-name church-name--sub" x="405" y="146">COMMUNITY CHURCH</text>
  </g>

  <!-- edge bubbles -->
  <g class="edge-bubbles" fill="url(#bubble)">
    <circle cx="0" cy="253" r="84"/>
    <circle cx="75" cy="316" r="39"/>
    <circle cx="777" cy="564" r="40"/>
    <circle cx="835" cy="632" r="84"/>
  </g>

  <!-- event badge -->
  <g class="badge">
    <circle class="badge__ring" cx="424.5" cy="495" r="205" fill="none" stroke="url(#badge)" stroke-width="13" stroke-linecap="round" stroke-dasharray="45 22"/>
    <circle class="badge__disc" cx="424.5" cy="495" r="168" fill="url(#badge)"/>
    <circle class="badge__bubble" cx="592" cy="337" r="77" fill="url(#bubble)" stroke="var(--paper)" stroke-width="13"/>
    <g class="badge__bubble-cluster" fill="url(#bubble)" stroke="var(--paper)" stroke-width="13">
      <circle cx="147" cy="524" r="16" stroke="none"/>
      <circle cx="153" cy="653" r="32" stroke="none"/>
      <circle cx="215" cy="582" r="77"/>
    </g>
    <text class="event-free" x="424.5" y="397" text-anchor="middle">FREE</text>
    <text class="event-title" x="424.5" y="504" text-anchor="middle">TOTZ</text>
    <text class="event-title event-title--outline" x="428.5" y="509" text-anchor="middle">TOTZ</text>
    <text class="event-subtitle" x="424.5" y="582" text-anchor="middle">JAM</text>
  </g>

  <!-- footer band -->
  <circle class="band band--bottom" cx="424.5" cy="1246" r="445" fill="url(#band-bottom)"/>

  <g class="details">
    <text class="event-date" x="424.5" y="913" text-anchor="middle">20 AUG</text>
    <text class="event-time" x="424.5" y="963" text-anchor="middle">10 AM - 2 PM</text>
    <text class="activity" x="176" y="1040">ROCK WALL</text>
    <text class="activity" x="341" y="1040">-</text>
    <text class="activity" x="393" y="1040">RIDES</text>
    <text class="activity" x="486" y="1040">-</text>
    <text class="activity" x="518" y="1040">BUNGEE JUMP</text>
    <text class="activity" x="176" y="1103">INFLATABLES</text>
    <text class="activity" x="341" y="1103">-</text>
    <text class="activity" x="393" y="1103">FOOD</text>
  </g>
</svg>
</body>
</html>
```